Design a label for a range of honey under :BRIGHT MEADOW HONEY. (Original quirky different)

Create a label for a range of honey products under the brand BRIGHT MEADOW HONEY.
Iam the beekeeper and want to sell for the local New Zealand market directly to the consumer, online mainly.
Brand position: A contemporary honey, a fresh look for a simple product, like nature intended, nothing taken out, nothing added. Doesnt take itself seriously.
Personality: Contemporary, fresh, modern, free and fun,loving. Doesnt take itself seriously, loving, generous, upbeat, provide enjoyment, life ...
Brand value: Straight up, keep it simple, generous, different,
Label: Modern twist of nature and goodness (no straight picture of nature) quirky?, use of slogan? ( Nature in a pot / More than just honey / Taste of nature / It's all good...
Need to stand out, make you smile, be noticed, different...

Target Market(s)

Online direct customer.

Requirements
Must have
• legal requirements for NZ labeling attached.
A twist and quirky side...
Should not have
• Basic picture of nature.
Straight forward boring everybody else's feel.

```html
<!DOCTYPE html>
<html lang="en">
<head>
<meta charset="utf-8">
<title>Bright Meadow Honey – Label Range</title>
<link rel="stylesheet" href="https://fonts.googleapis.com/css2?family=Kaushan+Script&family=Tinos&display=swap">
<style>
  :root {
    --backdrop: #5e4331;
    --cream: #f1ede3;
    --cream-speck: #cfc9bd;
    --cream-line: #1c1a18;
    --cream-ink: #141210;
    --cocoa: #2b201d;
    --cocoa-line: #f3cf0a;
    --cocoa-ink: #f6d40e;
    --art-cream: #d9d4ca;
    --art-cocoa: #4a3b36;
  }
  * { margin: 0; padding: 0; box-sizing: border-box; }
  html, body { width: 1200px; height: 840px; overflow: hidden; }
  body {
    background: var(--backdrop);
    position: relative;
  }
  .label {
    position: absolute;
    top: 134px;
    width: 500px;
    height: 572px;
    filter: drop-shadow(0 10px 18px rgba(0, 0, 0, 0.35));
  }
  .label--cream { left: 70px; }
  .label--cocoa { left: 630px; }
  .label__shape { position: absolute; inset: 0; width: 100%; height: 100%; }
  .label__art {
    position: absolute;
    left: 30px; top: 96px;
    width: 400px; height: 130px;
    border-radius: 14px;
  }
  .label--cream .label__art { background: linear-gradient(135deg, var(--art-cream), #e9e5db); }
  .label--cocoa .label__art { background: linear-gradient(135deg, var(--art-cocoa), #352925); }
  .label__brand {
    position: absolute;
    left: 40px; right: 30px; top: 236px;
    font-family: "Kaushan Script", cursive;
    font-weight: 400;
    line-height: 1;
  }
  .brand__line { display: block; }
  .brand__line--small {
    font-size: 36px;
    text-align: right;
    padding-right: 20px;
  }
  .brand__line--large {
    font-size: 150px;
    text-align: center;
    margin-top: -18px;
  }
  .label--cream .label__brand { color: var(--cream-ink); }
  .label--cocoa .label__brand { color: var(--cocoa-ink); }
  .label__weight {
    position: absolute;
    left: 0; right: 0; top: 448px;
    text-align: center;
    font-family: "Tinos", serif;
    font-size: 34px;
  }
  .label--cream .label__weight { color: var(--cream-ink); }
  .label--cocoa .label__weight { color: var(--cocoa-ink); }
</style>
</head>
<body>

  <section class="label label--cream">
    <svg class="label__shape" viewBox="0 0 500 572" aria-hidden="true">
      <polygon points="0,80 250,0 500,80 500,492 250,572 0,492" fill="var(--cream)"/>
      <polyline points="0,112 250,34 500,112" fill="none" stroke="var(--cream-line)" stroke-width="2.5"/>
      <polyline points="0,460 250,538 500,460" fill="none" stroke="var(--cream-line)" stroke-width="2.5"/>
    </svg>
    <div class="label__art" role="img" aria-label="Illustration of a branch with a hanging beehive and cartoon bees flying around it"></div>
    <h1 class="label__brand">
      <span class="brand__line brand__line--small">Bright Meadow</span>
      <span class="brand__line brand__line--large">Honey</span>
    </h1>
    <p class="label__weight">200g</p>
  </section>

  <section class="label label--cocoa">
    <svg class="label__shape" viewBox="0 0 500 572" aria-hidden="true">
      <polygon points="0,80 250,0 500,80 500,492 250,572 0,492" fill="var(--cocoa)"/>
      <polyline points="0,112 250,34 500,112" fill="none" stroke="var(--cocoa-line)" stroke-width="3"/>
      <polyline points="0,460 250,538 500,460" fill="none" stroke="var(--cocoa-line)" stroke-width="3"/>
    </svg>
    <div class="label__art" role="img" aria-label="Illustration of a branch with a hanging beehive and cartoon bees flying around it, in light tones"></div>
    <h2 class="label__brand">
      <span class="brand__line brand__line--small">Bright Meadow</span>
      <span class="brand__line brand__line--large">Honey</span>
    </h2>
    <p class="label__weight">200g</p>
  </section>

</body>
</html>
```